Flyers

Modify Existing Flyer and create another for exterior company
Updates

Previous Brief has been updated- we want to update this existing one also

Target Market(s)

Exterior Remodeling Customers

Industry/Entity Type

Remodeling/Construction

```html
<!DOCTYPE html>
<html lang="en">
<head>
<meta charset="utf-8">
<title>Roofing and Exteriors Flyer</title>
<link rel="stylesheet" href="https://fonts.googleapis.com/css2?family=Exo+2:wght@800&family=Lato:wght@400;700;900&display=swap">
<style>
  :root {
    --ink: #0b0b0c;
    --orange: #f0542a;
    --blue: #1f6fd6;
    --blue-light: #3b8de8;
    --white: #ffffff;
    --page: #ffffff;
  }
  html, body {
    margin: 0;
    padding: 0;
    width: 1200px;
    height: 1177px;
    overflow: hidden;
    background: var(--page);
  }
  .flyer {
    position: absolute;
    left: 271px;
    top: 88px;
    width: 696px;
    height: 968px;
    background: var(--ink);
    overflow: hidden;
    font-family: "Lato", Arial, sans-serif;
    color: var(--white);
  }
  .flyer-shapes {
    position: absolute;
    inset: 0;
    width: 100%;
    height: 100%;
  }
  .services-title {
    position: absolute;
    left: 154px;
    top: 467px;
    margin: 0;
    font-family: "Exo 2", "Arial Black", sans-serif;
    font-weight: 800;
    font-size: 26px;
    line-height: 25px;
    letter-spacing: 0.5px;
  }
  .services-title::after {
    content: "";
    display: block;
    width: 162px;
    height: 3px;
    margin-top: 6px;
    background: var(--blue);
  }
  .service-list {
    position: absolute;
    left: 154px;
    top: 641px;
    margin: 0;
    padding: 0;
    list-style: none;
    font-size: 19px;
    line-height: 24px;
  }
  .service {
    position: relative;
    padding-left: 14px;
    font-weight: 900;
    text-transform: uppercase;
  }
  .service::before {
    content: "";
    position: absolute;
    left: 0;
    top: 7px;
    border-left: 6px solid var(--blue-light);
    border-top: 5px solid transparent;
    border-bottom: 5px solid transparent;
  }
  .service--orange { color: var(--orange); }
  .service--blue { color: var(--blue-light); }
  .service-sub {
    display: block;
    color: var(--white);
    font-weight: 400;
    text-transform: none;
  }
  .service + .service { margin-top: 23px; }
  .service--first { margin-top: -100px; }
  .benefits {
    position: absolute;
    left: 418px;
    top: 456px;
    width: 270px;
    margin: 0;
    padding: 0;
    list-style: none;
    font-size: 15.5px;
    line-height: 18px;
  }
  .benefit {
    position: relative;
    padding-left: 39px;
    min-height: 36px;
  }
  .benefit + .benefit { margin-top: 17px; }
  .benefit b { font-weight: 700; }
  .tick {
    position: absolute;
    left: 0;
    top: -3px;
    width: 26px;
    height: 24px;
  }
  .brand-name {
    position: absolute;
    left: 430px;
    top: 822px;
    width: 260px;
    margin: 0;
    text-align: center;
    font-weight: 900;
    font-size: 22px;
    line-height: 26px;
    color: var(--orange);
    text-transform: uppercase;
  }
  .contact {
    position: absolute;
    top: 913px;
    margin: 0;
    font-style: normal;
    font-weight: 700;
    font-size: 15.5px;
    line-height: 21px;
  }
  .contact--address { left: 232px; }
  .contact--direct { left: 508px; }
  .contact-line {
    display: flex;
    align-items: flex-start;
    gap: 6px;
  }
  .contact-icon {
    width: 13px;
    height: 15px;
    margin-top: 2px;
    flex: none;
  }
  .contact-indent { padding-left: 19px; }
</style>
</head>
<body>
<main class="flyer">
  <svg class="flyer-shapes" viewBox="0 0 580 822" preserveAspectRatio="none" aria-hidden="false">
    <defs>
      <linearGradient id="metal-tone" x1="0" y1="0" x2="0" y2="1">
        <stop offset="0" stop-color="#8d9196"/>
        <stop offset="0.5" stop-color="#c9ccd0"/>
        <stop offset="1" stop-color="#5f6368"/>
      </linearGradient>
      <linearGradient id="house-tone" x1="0" y1="0" x2="0" y2="1">
        <stop offset="0" stop-color="#4f86d6"/>
        <stop offset="0.45" stop-color="#c9ced2"/>
        <stop offset="0.7" stop-color="#9fb2a0"/>
        <stop offset="1" stop-color="#4f9a2c"/>
      </linearGradient>
      <linearGradient id="panel-tone" x1="0" y1="0" x2="0" y2="1">
        <stop offset="0" stop-color="#3e78d2"/>
        <stop offset="0.55" stop-color="#6d6a9a"/>
        <stop offset="1" stop-color="#e4663a"/>
      </linearGradient>
      <linearGradient id="thumb-home" x1="0" y1="0" x2="0" y2="1">
        <stop offset="0" stop-color="#7fb2e6"/><stop offset="0.6" stop-color="#7a6553"/><stop offset="1" stop-color="#b9a58f"/>
      </linearGradient>
      <linearGradient id="thumb-gutter" x1="0" y1="0" x2="0" y2="1">
        <stop offset="0" stop-color="#c98fa0"/><stop offset="0.5" stop-color="#f2ede6"/><stop offset="1" stop-color="#d8cfc4"/>
      </linearGradient>
      <linearGradient id="thumb-deck" x1="0" y1="0" x2="0" y2="1">
        <stop offset="0" stop-color="#3f72c9"/><stop offset="0.5" stop-color="#d9dde0"/><stop offset="1" stop-color="#7a5a3e"/>
      </linearGradient>
      <linearGradient id="thumb-storm" x1="0" y1="0" x2="0" y2="1">
        <stop offset="0" stop-color="#9db5d0"/><stop offset="0.5" stop-color="#6b5a4c"/><stop offset="1" stop-color="#8f8579"/>
      </linearGradient>
    </defs>

    <polygon points="0,0 580,0 580,4 0,172" fill="#ffffff"/>
    <polygon points="0,0 548,0 0,156" fill="url(#metal-tone)" role="img" aria-label="Close-up photo of grey metal roofing panels"/>
    <polygon points="0,156 548,0 580,0 580,6 100,212 0,172" fill="#ffffff"/>
    <polygon points="100,215 580,8 580,405 335,304" fill="url(#house-tone)" role="img" aria-label="Photo of a white house with a pitched tiled roof and green lawn"/>
    <polygon points="335,304 580,405 580,412 335,310" fill="#ffffff"/>
    <polygon points="335,310 580,412 580,822 335,822" fill="url(#panel-tone)"/>

    <rect x="0" y="350" width="108" height="97" fill="url(#thumb-home)" role="img" aria-label="Photo of a two-storey home"/>
    <rect x="0" y="452" width="108" height="93" fill="url(#thumb-gutter)" role="img" aria-label="Photo of white gutters and roof edge"/>
    <rect x="0" y="550" width="108" height="95" fill="url(#thumb-deck)" role="img" aria-label="Photo of a house with a wooden deck"/>
    <rect x="0" y="650" width="108" height="95" fill="url(#thumb-storm)" role="img" aria-label="Photo of a storm-damaged building"/>

    <g class="service-icons" fill="none" stroke="#ffffff" stroke-width="2.2" stroke-linejoin="round" stroke-linecap="round">
      <g transform="translate(44,245)">
        <circle r="33" fill="#ffffff" stroke="none"/><circle r="30" fill="var(--blue)" stroke="none"/><circle r="26" fill="var(--orange)" stroke="none"/>
        <path d="M-14,6 L0,-10 L14,6 M-10,2 V10 H10 V2 M-6,-2 H6 M-8,4 H8"/>
      </g>
      <g transform="translate(124,270)">
        <circle r="33" fill="#ffffff" stroke="none"/><circle r="30" fill="var(--blue)" stroke="none"/><circle r="26" fill="var(--orange)" stroke="none"/>
        <path d="M-13,0 L0,-12 L13,0 M-9,-3 V12 H9 V-3 M-4,2 H4 V8 H-4 Z"/>
      </g>
      <g transform="translate(201,305)">
        <circle r="33" fill="#ffffff" stroke="none"/><circle r="30" fill="var(--blue)" stroke="none"/><circle r="26" fill="var(--orange)" stroke="none"/>
        <path d="M-10,-12 H10 V12 H-10 Z M-4,-12 V12 M3,-12 V12 M-10,-2 H10"/>
      </g>
      <g transform="translate(279,335)">
        <circle r="33" fill="#ffffff" stroke="none"/><circle r="30" fill="var(--blue)" stroke="none"/><circle r="26" fill="var(--orange)" stroke="none"/>
        <path d="M-13,0 L0,-12 L13,0 M-9,-3 V12 H9 V-3 M-2,-6 L2,0 L-1,4 L3,10"/>
      </g>
    </g>

    <polygon points="0,822 492,597 580,655 580,822" fill="var(--blue)"/>
    <polygon points="22,822 494,662 580,706 580,822" fill="var(--ink)"/>
  </svg>

  <h2 class="services-title">OUR<br>SERVICES</h2>

  <ul class="service-list">
    <li class="service service--orange service--first">Roof Installation<br>and Repair
      <span class="service-sub">Asphalt Roofing</span>
      <span class="service-sub">Metal Roofing</span>
    </li>
    <li class="service service--blue">Exterior Services</li>
    <li class="service service--orange">Siding &amp; Decking</li>
    <li class="service service--blue">Storm Damage</li>
  </ul>

  <ul class="benefits">
    <li class="benefit"><svg class="tick" viewBox="0 0 26 24"><rect x="1" y="5" width="18" height="18" fill="#ffffff"/><path d="M5,13 L10,19 L24,2" fill="none" stroke="#1a1a1a" stroke-width="3"/></svg>We have over<br><b>25 years of experience</b></li>
    <li class="benefit"><svg class="tick" viewBox="0 0 26 24"><rect x="1" y="5" width="18" height="18" fill="#ffffff"/><path d="M5,13 L10,19 L24,2" fill="none" stroke="#1a1a1a" stroke-width="3"/></svg>We're <b>licensed and insured</b></li>
    <li class="benefit"><svg class="tick" viewBox="0 0 26 24"><rect x="1" y="5" width="18" height="18" fill="#ffffff"/><path d="M5,13 L10,19 L24,2" fill="none" stroke="#1a1a1a" stroke-width="3"/></svg>We take pride in doing <b>quality work for an affordable price</b></li>
    <li class="benefit"><svg class="tick" viewBox="0 0 26 24"><rect x="1" y="5" width="18" height="18" fill="#ffffff"/><path d="M5,13 L10,19 L24,2" fill="none" stroke="#1a1a1a" stroke-width="3"/></svg>We have <b>financing options</b> available</li>
    <li class="benefit"><svg class="tick" viewBox="0 0 26 24"><rect x="1" y="5" width="18" height="18" fill="#ffffff"/><path d="M5,13 L10,19 L24,2" fill="none" stroke="#1a1a1a" stroke-width="3"/></svg>We'll be glad to give you<br><b>a no-obligation estimate</b></li>
  </ul>

  <p class="brand-name">Northgate<br>Roofing and Exteriors</p>

  <address class="contact contact--address">
    <span class="contact-line"><svg class="contact-icon" viewBox="0 0 13 15"><path d="M6.5,15 C2,9 1,7 1,5.5 A5.5,5.5 0 0 1 12,5.5 C12,7 11,9 6.5,15 Z" fill="#f5a623"/><circle cx="6.5" cy="5.5" r="2" fill="#0b0b0c"/></svg>218 Harlow Creek Drive,</span>
    <span class="contact-line contact-indent">Suite 12C, Maple Ridge, IA 50399</span>
  </address>

  <address class="contact contact--direct">
    <span class="contact-line"><svg class="contact-icon" viewBox="0 0 13 15"><path d="M2,2 L5,1.5 L6,5 L4.3,6.2 C5,8.5 6.3,9.8 8.2,10.6 L9.5,9 L12.5,10.5 L12,13.5 C6,13.5 1.5,8.5 2,2 Z" fill="#f5a623"/></svg>(555) 014-2287</span>
    <span class="contact-line"><svg class="contact-icon" viewBox="0 0 13 15"><circle cx="6.5" cy="7.5" r="5.5" fill="#f5a623"/><path d="M1,7.5 H12 M6.5,2 C4,5 4,10 6.5,13 C9,10 9,5 6.5,2" fill="none" stroke="#0b0b0c" stroke-width="1"/></svg>northgateroofs.com</span>
  </address>
</main>
</body>
</html>
```